Webdesign für K&L Vendora GmbH
Zielgruppe
- Partner für moderne Automaten- und Verpflegungslösungen in Unternehmen
- Zielgruppe sind Unternehmen, welche Versorgungskonzepte schaffen, die optimal auf die Bedürfnisse von Mitarbeitenden, Kunden und Gästen abgestimmt sind
Aufgabenstellung
- KEINE Kopie der alten Webseite
- Farbkonzept gern in sanften Kaffeetönen kombiniert mit Weiß
- Klare Struktur der Webseite

```html
<!DOCTYPE html>
<html lang="de">
<head>
<meta charset="utf-8">
<title>K&amp;L Vendora GmbH – Webdesign</title>
<link href="https://fonts.googleapis.com/css2?family=Inter:wght@400;500;600;700;800&display=swap" rel="stylesheet">
<style>
  :root{
    --navy:#0d1f5c;
    --blue:#6e95d1;
    --mist:#eceff4;
    --ink:#0a0a0a;
    --white:#ffffff;
    --page:#fdfdfd;
  }
  *{margin:0;padding:0;box-sizing:border-box}
  html,body{width:1200px;height:1200px;overflow:hidden;background:var(--page)}
  body{position:relative;font-family:"Inter",sans-serif;color:var(--ink)}

  .site-mockup{position:absolute;left:72px;top:102px;width:1064px;height:597px;background:var(--white);
    box-shadow:0 14px 40px rgba(0,0,0,.16);overflow:hidden}

  .site-header{position:absolute;left:0;top:0;width:100%;height:83px;background:var(--white)}
  .brand{position:absolute;left:63px;top:14px;display:flex;align-items:center;gap:14px}
  .brand-dot{width:58px;height:58px;border-radius:50%;background:var(--mist)}
  .brand-name{font-weight:700;font-size:17px;color:var(--ink)}
  .main-nav a{position:absolute;top:28px;font-weight:600;font-size:14.5px;color:var(--ink);text-decoration:none}
  .main-nav .is-active{border-bottom:2px solid var(--blue);padding-bottom:1px}
  .menu-toggle{position:absolute;left:1025px;top:32px;width:14px;height:12px}
  .contact-pill{position:absolute;left:818px;top:60px;width:246px;height:23px;background:var(--blue);
    border-radius:12px 0 0 0;color:var(--white);font-size:10.5px;font-weight:600;display:flex;align-items:center;gap:17px;padding-left:14px}

  .hero{position:absolute;left:0;top:83px;width:100%;height:514px;
    background:linear-gradient(90deg,#e6e1d2 0%,#d7d4bf 25%,#c9b8a0 48%,#a8917a 62%,#5d5a55 78%,#3a3d42 100%)}
  .hero-copy{position:absolute;left:51px;top:0;width:480px}
  .hero-badge{position:absolute;left:0;top:72px;width:48px;height:48px;border-radius:50%;background:var(--mist)}
  .hero-title{position:absolute;top:138px;font-weight:800;font-size:33px;line-height:40px;letter-spacing:-.3px;white-space:nowrap}
  .hero-lead{position:absolute;top:232px;font-weight:500;font-size:20px;line-height:24px;white-space:nowrap}
  .hero-text{position:absolute;top:300px;width:340px;font-size:11.6px;line-height:16.5px;white-space:nowrap}
  .cta{position:absolute;left:2px;top:388px;width:131px;height:43px;border-radius:22px;background:var(--navy);
    color:var(--white);font-weight:600;font-size:14px;display:flex;align-items:center;justify-content:center}
  .call-bubble{position:absolute;left:370px;top:352px;width:126px;height:126px;border-radius:50%;background:var(--blue);
    color:var(--white);display:flex;flex-direction:column;align-items:center;justify-content:center;transform:rotate(12deg);
    font-size:12px;line-height:14px;text-align:center}
  .call-bubble strong{font-weight:700;font-size:12.5px}

  .lockup-dot{position:absolute;left:91px;top:855px;width:190px;height:190px;border-radius:50%;background:var(--mist)}
  .lockup-name{position:absolute;left:311px;top:888px;font-weight:700;font-size:52px;line-height:58px;
    color:var(--ink);letter-spacing:-.5px;white-space:nowrap}
  .brand-mark{position:absolute;left:805px;top:817px;width:266px;height:266px;border-radius:50%;background:var(--mist)}
</style>
</head>
<body>
  <section class="site-mockup">
    <header class="site-header">
      <div class="brand"><span class="brand-dot"></span><span class="brand-name">K&amp;L Vendora GmbH</span></div>
      <nav class="main-nav">
        <a class="is-active" style="left:457px">Home</a>
        <a style="left:571px">Produkte</a>
        <a style="left:698px">Über Uns</a>
        <a style="left:834px">Kontakt</a>
      </nav>
      <svg class="menu-toggle" viewBox="0 0 14 12" aria-label="Menü"><rect y="0" width="14" height="2" fill="#0a0a0a"/><rect y="5" width="14" height="2" fill="#0a0a0a"/><rect y="10" width="14" height="2" fill="#0a0a0a"/></svg>
      <div class="contact-pill"><span>+49 30 5550199</span><span>info@kl-vendora.de</span></div>
    </header>

    <div class="hero" role="img" aria-label="Foto: lächelnde Frau bedient einen Snackautomaten im Freien">
      <div class="hero-copy">
        <span class="hero-badge"></span>
        <h1 class="hero-title">MODERNE AUTOMATEN<br>FÜR UNTERNEHMEN</h1>
        <p class="hero-lead">Kaffee, Getränke und Snacks<br>mit Rundum-Service</p>
        <p class="hero-text">Wir treffen mit Ihnen eine bedarfsgerechte Auswahl an<br>Heißgetränkeautomaten, Kaltgetränkeautomaten,<br>Snack- und Speiseautomaten, sowie für Wasserspender<br>in verschiednen Varianten.</p>
        <span class="cta">Mehr erfahren</span>
      </div>
      <div class="call-bubble"><span>Rufen Sie uns<br>an unter:</span><strong>+49 30 5550199</strong></div>
    </div>
  </section>

  <span class="lockup-dot"></span>
  <p class="lockup-name">K&amp;L<br>Vendora GmbH</p>
  <span class="brand-mark"></span>
</body>
</html>
```